Clerical Business Card Design

I have just started a new business focusing on Clerical / Administration Support for Small to Medium sized Businesses. I can provide support not just only my local area but anywhere as long as it is able to be done over the internet/email. I am the only person working in the business.
I would like to see some designs that are bright in colour yet a clean fresh design. The design should communicate balance.
Updates

Target Market(s)

Small to Medium sized Professional Businesses

Industry/Entity Type

Business

Contact Information for Business Card

Business Name: Vormley's Clerical
Statement: Providing Balanced Efficient Support
My Name: Ilsa Vormley
Phone: 0418 571 924 or 02 6519 4027
Email: vormleysclerical@plimmet.com.au

Colors

Designer to choose colors to be used in the design.

Requirements
Must have
• I'm open to suggestions
Nice to have
• I would like to see maybe something done with the two "C" in the business name whether that could be a focus of difference
Should not have
• Cartoon type pictures

```html
<!DOCTYPE html>
<html lang="en">
<head>
<meta charset="utf-8">
<title>Vormley's Clerical – Business Card</title>
<link rel="stylesheet" href="https://fonts.googleapis.com/css2?family=Archivo+Narrow:wght@400&family=Archivo:wght@400&display=swap">
<style>
  :root {
    --card-lime: #a4ff00;
    --ink: #000000;
    --emblem-violet: #8624ff;
  }
  html, body {
    margin: 0;
    padding: 0;
    width: 1200px;
    height: 741px;
    overflow: hidden;
    background: var(--card-lime);
  }
  .business-card {
    display: block;
    width: 1200px;
    height: 741px;
    background: var(--card-lime);
  }
  .tagline {
    font-family: "Archivo Narrow", "Arial Narrow", sans-serif;
    font-size: 58px;
    fill: var(--ink);
  }
  .contact-line {
    font-family: "Archivo", Arial, sans-serif;
    font-size: 34px;
    fill: var(--ink);
  }
  .emblem-area {
    fill: var(--emblem-violet);
  }
</style>
</head>
<body>
<svg class="business-card" width="1200" height="741" viewBox="0 0 1200 741" xmlns="http://www.w3.org/2000/svg">
  <text class="tagline" x="39" y="117" textLength="1131" lengthAdjust="spacingAndGlyphs">Vormley's Clerical Statement: Providing Balanced Efficient Support</text>

  <g role="img" aria-label="Purple leaf emblem">
    <rect class="emblem-area" x="278" y="222" width="576" height="257" rx="128" ry="128"/>
  </g>

  <g class="contact-block">
    <text class="contact-line" x="134" y="641" textLength="166" lengthAdjust="spacingAndGlyphs">NAME</text>
    <text class="contact-line" x="357" y="641" textLength="400" lengthAdjust="spacingAndGlyphs">-Ilsa Vormley</text>

    <text class="contact-line" x="134" y="666" textLength="204" lengthAdjust="spacingAndGlyphs">PHONe</text>
    <text class="contact-line" x="355" y="666" textLength="388" lengthAdjust="spacingAndGlyphs">-02 6519 4027</text>

    <text class="contact-line" x="355" y="693" textLength="385" lengthAdjust="spacingAndGlyphs">-0418 571 924</text>

    <text class="contact-line" x="134" y="721" textLength="134" lengthAdjust="spacingAndGlyphs">MAIL</text>
    <text class="contact-line" x="357" y="721" textLength="816" lengthAdjust="spacingAndGlyphs">-vormleysclerical@plimmet.com.au</text>
  </g>
</svg>
</body>
</html>
```